Personal contact Business card design needed

I work in the Property Industry - specifically Property Management.

I need a card I can hand out to colleagues at networking events, meetings, training courses etc. that will provide my contact details.

Target Market(s)

Professional colleagues / potential clients / employers

Industry/Entity Type

Training

Contact Information for Business Card

I need a simple and professional card to give to professional network contacts at meetings, interviews etc.

The card should include my photograph, name, mobile number, email address and Careerloom address.

I would like appropriate professional colours. Something feminine but not too 'frilly' or 'girly'

Requirements
Must have
• Photograph of myself.
I want it to be simple,perhaps a small icon for each contact detail such as
Email icon
Careerloom icon
Mobile number

```html
<!DOCTYPE html>
<html lang="en">
<head>
<meta charset="utf-8">
<title>Maree Lund – Property Management</title>
<link rel="stylesheet" href="https://fonts.googleapis.com/css2?family=Kalam:wght@700&family=Playball&display=swap">
<style>
  :root {
    --white: #ffffff;
    --ink: #111111;
    --header-yellow: #ffffc6;
    --panel-peach: #ffcc99;
    --photo-light: #d9d4cd;
    --photo-dark: #3a2320;
    --icon-blue: #3a7fc4;
    --icon-grey: #4a4a4a;
  }
  html, body {
    margin: 0;
    padding: 0;
    overflow: hidden;
    background: var(--white);
  }
  .card {
    position: relative;
    width: 1200px;
    height: 674px;
    background: var(--white);
    overflow: hidden;
    font-family: "Kalam", cursive;
    color: var(--ink);
  }
  .portrait {
    position: absolute;
    left: 29px;
    top: 29px;
    width: 487px;
    height: 380px;
    background: radial-gradient(ellipse at 50% 55%, #8a5a4c 0%, var(--photo-dark) 45%, transparent 46%),
                linear-gradient(180deg, var(--photo-light) 0%, #cfc9c1 100%);
  }
  .name {
    position: absolute;
    left: 0;
    width: 551px;
    top: 420px;
    margin: 0;
    text-align: center;
    font-family: "Playball", cursive;
    font-weight: 400;
    font-size: 64px;
    line-height: 1;
  }
  .role {
    position: absolute;
    left: 0;
    width: 551px;
    top: 522px;
    margin: 0;
    text-align: center;
    font-family: "Playball", cursive;
    font-size: 24px;
  }
  .contact-header {
    position: absolute;
    left: 551px;
    top: 0;
    width: 649px;
    height: 251px;
    background: var(--header-yellow);
    display: flex;
    align-items: center;
    justify-content: center;
  }
  .contact-header h2 {
    margin: 0 0 8px 0;
    font-size: 82px;
    font-weight: 700;
    font-style: italic;
    letter-spacing: 2px;
  }
  .contact-panel {
    position: absolute;
    left: 554px;
    top: 256px;
    width: 646px;
    height: 418px;
    background: var(--panel-peach);
  }
  .contact-row {
    position: absolute;
    left: 10px;
    display: flex;
    align-items: center;
    gap: 8px;
    font-size: 31px;
    font-weight: 700;
    font-style: italic;
    white-space: nowrap;
    letter-spacing: 1px;
  }
  .contact-row.phone { top: 52px; }
  .contact-row.email { top: 150px; font-size: 28px; }
  .contact-row.network { top: 262px; font-size: 26px; letter-spacing: 0; }
  .contact-row svg { flex: none; }
</style>
</head>
<body>
<div class="card">
  <div class="portrait" role="img" aria-label="Portrait photograph of Maree Lund"></div>
  <h1 class="name">Maree Lund</h1>
  <p class="role">Property Management</p>

  <div class="contact-header"><h2>Contact:</h2></div>

  <div class="contact-panel">
    <div class="contact-row phone">
      <svg width="44" height="56" viewBox="0 0 44 56" aria-hidden="true">
        <rect x="4" y="14" width="24" height="40" rx="3" fill="var(--icon-grey)"/>
        <rect x="8" y="18" width="16" height="12" fill="#dfe6ee"/>
        <g fill="#dfe6ee">
          <rect x="8" y="34" width="4" height="3"/><rect x="14" y="34" width="4" height="3"/><rect x="20" y="34" width="4" height="3"/>
          <rect x="8" y="40" width="4" height="3"/><rect x="14" y="40" width="4" height="3"/><rect x="20" y="40" width="4" height="3"/>
          <rect x="8" y="46" width="4" height="3"/><rect x="14" y="46" width="4" height="3"/><rect x="20" y="46" width="4" height="3"/>
        </g>
        <line x1="24" y1="14" x2="30" y2="6" stroke="var(--icon-grey)" stroke-width="3"/>
        <path d="M30 2 a8 8 0 0 1 8 8" fill="none" stroke="var(--icon-blue)" stroke-width="2"/>
        <path d="M30 -3 a13 13 0 0 1 13 13" fill="none" stroke="var(--icon-blue)" stroke-width="2"/>
      </svg>
      <span>: 0491 570 156</span>
    </div>

    <div class="contact-row email">
      <svg width="50" height="56" viewBox="0 0 50 56" aria-hidden="true">
        <rect x="6" y="6" width="36" height="30" rx="3" fill="#eef3f8" stroke="#9fb3c8" stroke-width="2"/>
        <circle cx="24" cy="21" r="9" fill="none" stroke="var(--icon-blue)" stroke-width="3"/>
        <circle cx="24" cy="21" r="3" fill="var(--icon-blue)"/>
        <path d="M2 30 L24 44 L46 30 L46 54 L2 54 Z" fill="var(--icon-blue)"/>
        <path d="M2 54 L20 40 M46 54 L28 40" stroke="#2a5f96" stroke-width="2"/>
      </svg>
      <span>: maree@mareelundmail.com.au</span>
    </div>

    <div class="contact-row network">
      <svg width="46" height="46" viewBox="0 0 46 46" aria-hidden="true">
        <rect x="1" y="1" width="44" height="44" rx="4" fill="var(--icon-blue)"/>
      </svg>
      <span>:au.careerloom.com/in/mareelundaustralia</span>
    </div>
  </div>
</div>
</body>
</html>
```